Brivora Australia Company Values.

We have just completed our company purpose, beliefs and values (for the first time, we have not had these before)
We are now wanting to add images to each company value as a visual
so they are easily identified and understood for all our staff - we need them to remember the 5 Values.
We are a manufacturer of dental materials and infection control products, based in Melbourne.

What we would like:
- A Poster (that can be placed in our staff lunch rooms)
- The values to be lined up Horizontally
- Image on the top of the words
- Wording does not all need to be the same text font
- No image photographs - please use image graphics
- No images with people
- No dental related graphics

Target audience: Brivora staff

Our Values are:
Think Big
Have a go, learn and adapt
If you're gonna do it, do it bloody well
Empower Others
Be a good human

I have uploaded some examples.

Target Market(s)

Brivora Team members

Industry/Entity Type

Healthcare

Colors

Designer to choose colors to be used in the design.

Requirements
Must have
• Clear horizontal layout, space between each value
Should not have
• No images with humans or dental

```html
<!DOCTYPE html>
<html lang="en">
<head>
<meta charset="utf-8">
<title>Brivora Australia – Company Values</title>
<link rel="stylesheet" href="https://fonts.googleapis.com/css2?family=Barlow:wght@700&display=swap">
<style>
  :root {
    --bg: #f2f2f2;
    --white: #ffffff;
    --pink: #f28ab7;
    --pink-deep: #d9689b;
    --cyan: #3ac3d9;
    --cyan-deep: #22a4ba;
    --green: #8dc63f;
    --green-deep: #6eaa28;
    --blue: #3c96d2;
    --blue-deep: #2a7bb5;
    --coral: #f48582;
    --coral-deep: #dc6462;
    --shadow: rgba(120, 124, 132, 0.55);
  }
  * { margin: 0; padding: 0; box-sizing: border-box; }
  html, body {
    width: 1200px;
    height: 927px;
    overflow: hidden;
    background: var(--bg);
  }
  .poster {
    position: relative;
    width: 1200px;
    height: 927px;
    background: var(--bg);
    font-family: "Barlow", "Arial Narrow", sans-serif;
  }
  .floor-shadow {
    position: absolute;
    left: 120px;
    top: 705px;
    width: 960px;
    height: 90px;
    border-radius: 50%;
    background: radial-gradient(ellipse at center, var(--shadow) 0%, rgba(150,152,158,0.25) 45%, rgba(242,242,242,0) 72%);
  }
  .values {
    position: absolute;
    left: 129px;
    top: 262px;
    display: flex;
    gap: 8px;
  }
  .value-card {
    position: relative;
    width: 180.5px;
    height: 418px;
    border-radius: 14px;
    color: var(--white);
  }
  .value-card--think    { background: var(--pink);  --deep: var(--pink-deep); }
  .value-card--have-a-go{ background: var(--cyan);  --deep: var(--cyan-deep); }
  .value-card--do-well  { background: var(--green); --deep: var(--green-deep); }
  .value-card--empower  { background: var(--blue);  --deep: var(--blue-deep); }
  .value-card--human    { background: var(--coral); --deep: var(--coral-deep); }

  .value-badge {
    position: absolute;
    left: 50%;
    top: 44px;
    width: 130px;
    height: 130px;
    transform: translateX(-50%);
  }
  .value-badge .rim { fill: var(--deep); }
  .value-divider {
    position: absolute;
    left: 50%;
    top: 214px;
    width: 106px;
    height: 14px;
    transform: translateX(-50%);
  }
  .value-name {
    position: absolute;
    left: 0;
    right: 0;
    top: 258px;
    padding: 0 12px;
    text-align: center;
    font-size: 22px;
    font-weight: 700;
    line-height: 27.5px;
    letter-spacing: 0.1px;
  }
</style>
</head>
<body>
<main class="poster" aria-label="Brivora Australia company values">
  <div class="floor-shadow"></div>

  <svg width="0" height="0" style="position:absolute">
    <defs>
      <symbol id="badge-base" viewBox="0 0 130 130">
        <circle cx="65" cy="65" r="62" fill="none" stroke="#fff" stroke-width="2.5"/>
        <circle class="rim" cx="65" cy="65" r="55"/>
        <circle cx="63" cy="63" r="52" fill="#fff"/>
      </symbol>
      <symbol id="wave" viewBox="0 0 106 14">
        <path d="M2 7 q4.5 -6 9 0 t9 0 t9 0 t9 0 t9 0 t9 0 t9 0 t9 0 t9 0 t9 0 t9 0 t9 0" fill="none" stroke="#fff" stroke-width="2.4" stroke-linecap="round"/>
      </symbol>
    </defs>
  </svg>

  <section class="values">
    <article class="value-card value-card--think">
      <svg class="value-badge" viewBox="0 0 130 130" aria-hidden="true">
        <use href="#badge-base"/>
        <g fill="var(--pink)" stroke="var(--pink)">
          <path d="M63 49 a11 11 0 0 0 -7 19.5 v5 h14 v-5 a11 11 0 0 0 -7 -19.5z" stroke="none"/>
          <rect x="57" y="75" width="12" height="3" rx="1" stroke="none"/>
          <rect x="58.5" y="79.5" width="9" height="3" rx="1" stroke="none"/>
          <g stroke-width="2.4" stroke-linecap="round" fill="none">
            <line x1="63" y1="39" x2="63" y2="43"/>
            <line x1="50" y1="44" x2="52.5" y2="47"/>
            <line x1="76" y1="44" x2="73.5" y2="47"/>
            <line x1="44" y1="55" x2="48" y2="56"/>
            <line x1="82" y1="55" x2="78" y2="56"/>
          </g>
        </g>
      </svg>
      <svg class="value-divider" aria-hidden="true"><use href="#wave"/></svg>
      <h2 class="value-name">Think Big</h2>
    </article>

    <article class="value-card value-card--have-a-go">
      <svg class="value-badge" viewBox="0 0 130 130" aria-hidden="true">
        <use href="#badge-base"/>
        <path d="M82 45 L48 60 L62 64 L66 78 Z" fill="var(--cyan)"/>
      </svg>
      <svg class="value-divider" aria-hidden="true"><use href="#wave"/></svg>
      <h2 class="value-name">Have A<br>Go, Learn<br>And Adapt</h2>
    </article>

    <article class="value-card value-card--do-well">
      <svg class="value-badge" viewBox="0 0 130 130" aria-hidden="true">
        <use href="#badge-base"/>
        <path d="M63 45 l5.3 11.2 12.2 1.5 -9 8.5 2.3 12.1 -10.8 -6 -10.8 6 2.3 -12.1 -9 -8.5 12.2 -1.5z" fill="var(--green)" stroke="var(--green)" stroke-width="2.5" stroke-linejoin="round"/>
      </svg>
      <svg class="value-divider" aria-hidden="true"><use href="#wave"/></svg>
      <h2 class="value-name">If You're<br>Gonna Do<br>It, Do It<br>Bloody Well</h2>
    </article>

    <article class="value-card value-card--empower">
      <svg class="value-badge" viewBox="0 0 130 130" aria-hidden="true">
        <use href="#badge-base"/>
        <g fill="var(--blue)">
          <rect x="46" y="60" width="7" height="18" rx="1.5"/>
          <path d="M56 60 l7 -9 c1 -3 1 -6 3 -7 c3 -1 5 1 5 4 l-2 9 h9 c3 0 5 2.5 4.5 5 l-2.5 13 c-0.5 2 -2 3.5 -4 3.5 h-20 z"/>
        </g>
      </svg>
      <svg class="value-divider" aria-hidden="true"><use href="#wave"/></svg>
      <h2 class="value-name">Empower<br>Others</h2>
    </article>

    <article class="value-card value-card--human">
      <svg class="value-badge" viewBox="0 0 130 130" aria-hidden="true">
        <use href="#badge-base"/>
        <path d="M63 80 L47 64 a9.5 9.5 0 0 1 16 -11 a9.5 9.5 0 0 1 16 11 Z" fill="var(--coral)"/>
      </svg>
      <svg class="value-divider" aria-hidden="true"><use href="#wave"/></svg>
      <h2 class="value-name">Be A Good<br>Human</h2>
    </article>
  </section>
</main>
</body>
</html>
```